Business Cards

I'd like help creating business cards with the full logo "Veltrona Capital Partners" on the back of the card (navy background with white writing), and abbreviated logo "VCP" on the front. Would like to list name, title, phone number, email, and website listed on front of card. Would like to keep very simple. Front font Arial or similar.

```html
<!DOCTYPE html>
<html lang="en">
<head>
<meta charset="utf-8">
<title>Veltrona Capital Partners – Business Cards</title>
<link rel="stylesheet" href="https://fonts.googleapis.com/css2?family=Arimo:wght@400;700&family=Montserrat:wght@600;700&display=swap">
<style>
  :root {
    --stage: #1d1d1f;
    --navy: #1f3677;
    --navy-deep: #192c66;
    --navy-text: #1c3461;
    --ink: #1f1f24;
    --paper: #d3d4d7;
    --white: #ffffff;
  }
  * { box-sizing: border-box; margin: 0; padding: 0; }
  html, body {
    width: 900px; height: 1200px; overflow: hidden;
    background: var(--stage);
  }
  .card {
    position: absolute;
    left: 134px;
    width: 633px;
    height: 366px;
  }
  /* Back of card */
  .card-back {
    top: 210px;
    background: var(--navy);
    color: var(--white);
    font-family: "Montserrat", sans-serif;
  }
  .card-back .pattern-field {
    position: absolute; inset: 0;
    background: linear-gradient(90deg, var(--navy-deep) 0%, var(--navy) 55%, #2b4189 100%);
  }
  .wordmark {
    position: absolute; left: 0; right: 0; top: 128px;
    text-align: center;
  }
  .wordmark .name {
    display: block;
    font-weight: 700;
    font-size: 54px;
    letter-spacing: 2px;
    line-height: 1;
  }
  .wordmark .tagline {
    display: block;
    margin-top: 22px;
    font-weight: 600;
    font-size: 19px;
    letter-spacing: 8px;
    line-height: 1;
  }
  /* Front of card */
  .card-front {
    top: 624px;
    background: var(--paper);
    font-family: "Arimo", Arial, sans-serif;
    color: var(--ink);
  }
  .monogram {
    position: absolute; left: 47px; top: 52px;
    font-weight: 700;
    font-size: 66px;
    line-height: 1;
    letter-spacing: 1px;
    color: var(--navy-text);
  }
  .person {
    position: absolute; left: 360px; width: 240px; top: 155px;
    text-align: center;
  }
  .person .full-name {
    font-weight: 700; font-size: 30px; color: var(--navy-text); line-height: 1.1;
  }
  .person .role {
    margin-top: 6px; font-size: 14px; color: var(--ink);
  }
  .contacts {
    position: absolute; left: 46px; top: 270px;
    list-style: none;
    font-size: 15px; letter-spacing: 1px;
  }
  .contacts li {
    display: flex; align-items: center; gap: 4px;
    height: 23px;
  }
  .contacts svg { width: 12px; height: 12px; fill: var(--navy-text); }
</style>
</head>
<body>
  <section class="card card-back" aria-label="Card back">
    <div class="pattern-field" role="img" aria-label="Repeating faint VCP monogram pattern on navy"></div>
    <div class="wordmark">
      <span class="name">VELTRONA</span>
      <span class="tagline">CAPITAL PARTNERS</span>
    </div>
  </section>

  <section class="card card-front" aria-label="Card front">
    <div class="monogram">VCP</div>
    <div class="person">
      <p class="full-name">Dana Holbrook</p>
      <p class="role">Co-Founder and Managing Partner</p>
    </div>
    <ul class="contacts">
      <li>
        <svg viewBox="0 0 24 24" aria-hidden="true"><path d="M6.6 10.8a15 15 0 0 0 6.6 6.6l2.2-2.2a1 1 0 0 1 1-.25 11.4 11.4 0 0 0 3.6.57 1 1 0 0 1 1 1V20a1 1 0 0 1-1 1A17 17 0 0 1 3 4a1 1 0 0 1 1-1h3.5a1 1 0 0 1 1 1c0 1.25.2 2.45.57 3.57a1 1 0 0 1-.25 1z"/></svg>
        (555) 014-2290
      </li>
      <li>
        <svg viewBox="0 0 24 24" aria-hidden="true"><path d="M2 5h20v14H2z M2 5l10 8 10-8" fill="var(--navy-text)"/><path d="M3 6l9 7 9-7" fill="none" stroke="var(--paper)" stroke-width="1.6"/></svg>
        Dana.Holbrook@VeltronaCP.com
      </li>
      <li>
        <svg viewBox="0 0 24 24" aria-hidden="true"><circle cx="12" cy="12" r="10"/><path d="M2 12h20M12 2v20M12 2c-4 5-4 15 0 20M12 2c4 5 4 15 0 20M4 7h16M4 17h16" fill="none" stroke="var(--paper)" stroke-width="1.3"/></svg>
        www.VeltronaCP.com
      </li>
    </ul>
  </section>
</body>
</html>
```